A new updated business card. A good first impression for new customers to our business.

I need something unique. I will attached a picture of our old rubbish cards, and also our current Logo ( I think this needs an update if you have any ideas, its very basic and budget)The best way you will get to see my business is checking our Linkbook page, I don't really know what else to say, but anything you want to know, ask away.www.facebook.com/tkwsurfacewashing/

Target Market(s)

Home owners

Industry/Entity Type

Business

Contact Information for Business Card

T&K's Surface Washing & Paving Glazing
Mira 0462 318 905 mira@tkwsurfacewashing.com
Dunstan 0458 621 370 dunstan@tkwsurfacewashing.com

FB: www.facebook.com/tkwsurfacewashing/
Website: www.tkwsurfacewashing.net (This is pretty rubbish- we don't really use it)

100% customer satisfaction guaranteed

All aspects of Hi-Pressure Cleaning
Sealing & Re-Sealing
Roof Cleaning
Colour sealing
Decorative coatings

Free no obligation quotes

Requirements
Must have
• NO OBLIGATION FREE quotes
• 100% Customer satisfaction guaranteed
• Can you please add both names, contact details and email address on one card.
• Dunstan 0458 621 370
• dunstan@tkwsurfacewashing.com
• Mira 0462 318 905
• mira@tkwsurfacewashing.com
• Please change the services:
• Hot/Cold Hi-Pressure Cleaning
• Sealing & Re-Sealing
• Roof Cleaning
• Colour Sealing
• Decorative Coatings
• Concrete Honing
• Thanks
Nice to have
• Something a bit different, something eye catching.l

```html
<!DOCTYPE html>
<html lang="en">
<head>
<meta charset="UTF-8">
<title>T&amp;K's Surface Washing &amp; Paving Glazing – Business Card</title>
<link rel="stylesheet" href="https://fonts.googleapis.com/css2?family=Open+Sans:ital,wght@0,400;0,600;0,700;1,700&display=swap">
<style>
  :root {
    --page-bg: #e7e4df;
    --card-top: #c4dcee;
    --card-bottom: #e6eef4;
    --ink: #1c1f22;
    --ink-soft: #2e3338;
    --accent-red: #d3242a;
    --badge-red: #b81d22;
    --badge-gold: #c9962f;
    --social-blue: #3b5a98;
  }
  * { margin: 0; padding: 0; box-sizing: border-box; }
  html, body {
    width: 1200px;
    height: 969px;
    overflow: hidden;
    background: var(--page-bg);
    font-family: "Open Sans", Arial, sans-serif;
    color: var(--ink);
  }
  .business-card {
    position: absolute;
    left: 80px;
    top: 190px;
    width: 1040px;
    height: 592px;
    border-radius: 34px;
    overflow: hidden;
    box-shadow: 0 10px 30px rgba(0,0,0,0.18);
  }
  .card-surface {
    position: absolute;
    inset: 0;
    background: linear-gradient(160deg, var(--card-top) 0%, #d3e3ef 45%, var(--card-bottom) 100%);
  }
  .brand {
    position: absolute;
    left: 48px;
    top: 62px;
    display: flex;
    align-items: center;
    gap: 18px;
  }
  .brand-dot {
    width: 64px;
    height: 64px;
    border-radius: 50%;
    background: var(--accent-red);
    flex: none;
  }
  .brand-name {
    font-weight: 700;
    font-size: 30px;
    line-height: 1.15;
    color: var(--ink);
  }
  .contacts {
    position: absolute;
    left: 45px;
    top: 252px;
  }
  .contact-name {
    font-weight: 600;
    font-size: 36px;
    color: var(--accent-red);
    line-height: 1.2;
  }
  .contact-phone {
    font-weight: 400;
    font-size: 31px;
    line-height: 1.25;
    letter-spacing: 0.5px;
  }
  .contact-email {
    font-size: 26px;
    line-height: 1.45;
    color: var(--ink-soft);
  }
  .contact-block + .contact-block { margin-top: 4px; }
  .website {
    font-size: 26px;
    line-height: 1.5;
    margin-top: 4px;
    color: var(--ink-soft);
  }
  .social {
    position: absolute;
    left: 680px;
    top: 70px;
    display: flex;
    align-items: center;
    gap: 10px;
  }
  .social-square {
    width: 56px;
    height: 56px;
    border-radius: 8px;
    background: var(--social-blue);
  }
  .social-name {
    font-size: 22px;
    font-weight: 600;
    color: var(--ink);
  }
  .satisfaction-badge {
    position: absolute;
    left: 870px;
    top: 28px;
    width: 128px;
    height: 128px;
    border-radius: 50%;
    background: var(--badge-red);
    border: 8px solid var(--badge-gold);
  }
  .services {
    position: absolute;
    right: 38px;
    top: 240px;
    list-style: none;
    text-align: right;
  }
  .services li {
    font-size: 29px;
    line-height: 45px;
    padding-right: 28px;
    position: relative;
  }
  .services li::after {
    content: "";
    position: absolute;
    right: 4px;
    top: 21px;
    width: 9px;
    height: 9px;
    border-radius: 50%;
    background: var(--accent-red);
  }
  .free-quotes {
    position: absolute;
    right: 66px;
    top: 512px;
    font-weight: 700;
    font-style: italic;
    font-size: 32px;
    color: var(--accent-red);
  }
</style>
</head>
<body>
  <div class="business-card">
    <div class="card-surface" role="img" aria-label="Pale blue translucent card surface with soft water bubble texture"></div>

    <div class="brand">
      <span class="brand-dot"></span>
      <span class="brand-name">T&amp;K's Surface Washing<br>&amp; Paving Glazing</span>
    </div>

    <div class="social">
      <span class="social-square"></span>
      <span class="social-name">Linkbook</span>
    </div>
    <div class="satisfaction-badge" aria-label="Customer satisfaction guarantee badge"></div>

    <div class="contacts">
      <div class="contact-block">
        <div class="contact-name">Dunstan</div>
        <div class="contact-phone">0458 621 370</div>
        <div class="contact-email">dunstan@tkwsurfacewashing.com</div>
      </div>
      <div class="contact-block">
        <div class="contact-name">Mira</div>
        <div class="contact-phone">0462 318 905</div>
        <div class="contact-email">mira@tkwsurfacewashing.com</div>
      </div>
      <div class="website">www.tkwsurfacewashing.net</div>
    </div>

    <ul class="services">
      <li>Hot/Cold Hi-Pressure Cleaning</li>
      <li>Sealing &amp; Re-Sealing</li>
      <li>Roof Cleaning</li>
      <li>Colour Sealing</li>
      <li>Decorative Coatings</li>
      <li>Concrete Honing</li>
    </ul>

    <div class="free-quotes">Free no obligation quotes</div>
  </div>
</body>
</html>
```